Kestrel Dental personal information forms

We are a Dental Practice that require an update to our information forms, there are 3 versions of it.
I will attach our old ones, we need to keep the same information on there, we just want them to look better and use our current logo and colours.
Our website is www.kestreldental.net
Our facebook is www.friendnook.com/kestreldentalbrookplaza/
..................................................................................................

Target Market(s)

Everyone, easy to read

Industry/Entity Type

Dental Clinic

Colors
0692cd
34a6d7
cee9f5
ffffff
0255a3
3276b5

Requirements
Must have
• Logo
• Our colours
• same information as the uploaded versions
Should not have
• any other colour besides the blues, black and white

```html
<!DOCTYPE html>
<html lang="en">
<head>
<meta charset="utf-8">
<title>Kestrel Dental – Medical History Update Form</title>
<link rel="stylesheet" href="https://fonts.googleapis.com/css2?family=Lato:ital,wght@0,400;0,700;0,900;1,400&family=Nunito+Sans:wght@700;800&family=Nunito:wght@600&display=swap">
<style>
  :root{
    --navy:#0255a3;
    --sky:#0692cd;
    --aqua:#34a6d7;
    --ice:#cee9f5;
    --steel:#3276b5;
    --white:#ffffff;
    --ink:#1c1c1c;
    --body-font:'Lato', Arial, sans-serif;
    --head-font:'Nunito Sans', Arial, sans-serif;
    --band-font:'Nunito', Arial, sans-serif;
  }
  *{box-sizing:border-box;margin:0;padding:0}
  html,body{width:902px;height:1200px;overflow:hidden;background:var(--white)}
  body{font-family:var(--body-font);color:var(--ink)}
  .form-sheet{position:relative;width:902px;height:1200px;overflow:hidden;background:var(--white)}
  .abs{position:absolute}

  /* header */
  .header-band{left:0;top:0;width:902px;height:93px}
  .brand-name{left:96px;top:24px;font-size:36px;font-weight:700;color:var(--sky);letter-spacing:.5px}
  .practitioners{left:502px;top:22px;color:var(--white);font-weight:700;font-size:19px;line-height:24px}

  .hero-photo{left:0;top:93px;width:902px;height:147px;background:linear-gradient(90deg,#f4f6f8 0%,#e8ecef 30%,#f7f7f7 55%,var(--white) 62%)}
  .hero-photo .placeholder{position:absolute;left:28px;top:0;width:468px;height:147px;background:radial-gradient(ellipse at 45% 55%,#f1d2c6 0%,#dfb2a3 45%,#efe6e2 80%,transparent 100%)}
  .sticker-box{left:538px;top:141px;width:329px;height:60px;border:1px solid var(--aqua);background:var(--white);display:flex;align-items:center;justify-content:center;font-size:14px;font-weight:700;color:#333}

  .welcome-band{left:0;top:240px;width:902px;height:47px;background:var(--sky);color:var(--white);font-family:var(--band-font);font-size:25px;font-weight:600;text-align:center;line-height:47px;letter-spacing:.4px}
  .intro{left:35px;top:300px;width:845px;font-size:14.3px;line-height:17px;color:#333}
  .intro strong{color:var(--navy);font-weight:700}

  /* questionnaire */
  .blue-field{left:0;top:363px;width:902px;height:736px;background:var(--navy)}
  .card{left:41px;top:354px;width:820px;height:744px;background:var(--white);border:2px solid #222;border-radius:16px;overflow:hidden}
  .q-band{position:absolute;left:0;width:816px;background:var(--ice);display:flex;align-items:center}
  .q-text{font-family:var(--head-font);font-weight:800;font-size:14.5px;letter-spacing:.35px;color:#222;line-height:17px;padding-left:18px;width:700px}
  .q-text .hint{color:var(--navy)}
  .yes-no{position:absolute;right:0;top:0;height:100%;width:89px;background:var(--aqua);color:var(--white);font-size:14px;display:flex;align-items:center;justify-content:center}
  .answer{position:absolute;left:16px;width:788px;border:1px solid #444;background:var(--white)}

  .conditions{position:absolute;left:72px;top:256px;display:flex}
  .conditions ul{list-style:none;font-style:italic;font-size:11px;line-height:17.5px;color:#222}
  .col-1{width:184px}.col-2{width:195px}.col-3{width:178px}

  /* footer */
  .footer{left:0;top:1098px;width:902px;height:102px;background:var(--ice)}
  .declaration{left:61px;top:1110px;width:780px;font-size:13px;line-height:16px;color:#222}
  .sig-label{left:62px;top:1153px;font-size:13px;color:var(--navy);font-weight:700;white-space:nowrap}
  .sig-line{left:338px;top:1148px;width:278px;height:27px;border:1px solid var(--aqua);background:var(--white)}
  .date-label{left:645px;top:1151px;font-size:13px;color:var(--navy);font-weight:700}
  .date-line{left:688px;top:1145px;width:163px;height:27px;border:1px solid var(--aqua);background:var(--white)}
</style>
</head>
<body>
<main class="form-sheet">

  <svg class="abs header-band" width="902" height="93" viewBox="0 0 902 93" aria-hidden="true">
    <rect width="902" height="93" fill="#0255a3"/>
    <polygon points="0,0 372,0 448,93 0,93" fill="#ffffff"/>
    <polygon points="372,0 398,0 474,93 448,93" fill="#34a6d7"/>
    <polygon points="398,0 408,0 484,93 474,93" fill="#cee9f5"/>
  </svg>
  <div class="abs brand-name">Kestrel Dental</div>
  <div class="abs practitioners">Dr. Elias Thornbury &amp; Dr. Martin Oakes<br>Dental Surgeons</div>

  <div class="abs hero-photo">
    <div class="placeholder" role="img" aria-label="Close-up photo of a smiling mouth with white teeth and a dental mirror"></div>
  </div>
  <div class="abs sticker-box">Affix patient sticker here.</div>

  <div class="abs welcome-band">Welcome back to our practice!</div>
  <p class="abs intro"><strong>THIS INFORMATION IS CONFIDENTIAL</strong> and is necessary to enable us to offer you THE BEST POSSSIBLE CARE. now mandatory to have a written updated medical history every 2 years and we would appreciate your time in thoroughly completing this form.</p>

  <div class="abs blue-field"></div>
  <section class="abs card">
    <div class="q-band" style="top:0;height:48px">
      <p class="q-text" style="width:690px">Are you currently or have you taken any prescribed medication or dietary supplements in the last 12 months? <span class="hint">(If YES, please list below)</span></p>
      <span class="yes-no">YES/NO</span>
    </div>
    <div class="answer" style="top:57px;height:36px"></div>

    <div class="q-band" style="top:108px;height:29px">
      <p class="q-text" style="padding-left:26px">Allergies / Reactions? <span class="hint">( If YES, please list below )</span></p>
      <span class="yes-no">YES/NO</span>
    </div>
    <div class="answer" style="top:147px;height:37px;left:10px"></div>

    <div class="q-band" style="top:198px;height:34px;border-top:1px solid var(--aqua);border-bottom:1px solid var(--aqua)">
      <p class="q-text" style="width:800px">Have you ever had or are you suffering from any of the following? Please tick any that apply:</p>
    </div>
    <div class="conditions">
      <ul class="col-1"><li>Rheumatic fever</li><li>Diabetes</li><li>HIV Positive</li><li>Epilepsy</li><li>Kidney Disease</li><li>High cholesterol</li></ul>
      <ul class="col-2"><li>Asthma</li><li>Heart Attack</li><li>Cancer</li><li>Tuberculosis</li><li>High Blood Pressure</li><li>Pace-maker</li></ul>
      <ul class="col-3"><li>Radiation Therapy</li><li>Bleeding problems</li><li>Osteoporosis</li><li>Dizziness, fainting</li><li>Artificial joints</li><li>Heart rate problems</li></ul>
      <ul><li>Hepatitis A B or C</li><li>Respiratory problems</li><li>Heart murmur</li><li>Recent eye surgery</li></ul>
    </div>

    <div class="q-band" style="top:373px;height:34px">
      <p class="q-text">Do you have any disease, condition or problem not listed above?</p>
      <span class="yes-no">YES/NO</span>
    </div>
    <div class="answer" style="top:413px;height:34px"></div>

    <div class="q-band" style="top:466px;height:34px">
      <p class="q-text" style="padding-left:26px;width:720px">Have you had surgery or been to hospital in the last 5 years? (if YES, please give details)</p>
      <span class="yes-no">YES/NO</span>
    </div>
    <div class="answer" style="top:507px;height:34px"></div>

    <div class="q-band" style="top:550px;height:36px">
      <p class="q-text">For Women: Are you pregnant? If yes, how many months?</p>
      <span class="yes-no">YES/NO</span>
    </div>
    <div class="answer" style="top:596px;height:34px"></div>

    <div class="q-band" style="top:644px;height:34px">
      <p class="q-text">Do you currently or have you ever smoked?</p>
      <span class="yes-no">YES/NO</span>
    </div>
    <div class="answer" style="top:686px;height:34px;left:12px"></div>
  </section>

  <div class="abs footer"></div>
  <p class="abs declaration">The information that I have provided is to the best of my knowledge true and correct and I understand that it is my responsibility to inform of any changes in my medical status.</p>
  <span class="abs sig-label">Patient/Parent/Person Responsible Signature:</span>
  <div class="abs sig-line"></div>
  <span class="abs date-label">Date:</span>
  <div class="abs date-line"></div>

</main>
</body>
</html>
```